New Web Design Project open cart

We are about to start a new furniture selling website and it will be based on open cart . we mainly need two pages designing landing page & item page. so come up with your unique ideas and designs . Please make sure the design needs to be unique . no templates and themes . Will make the selected designer even happier if your design is selected. So basically over all it is going to be the new theme for our open cart base eCommerce website .we will appreciate if its responsive with some unique features .
SO as per request of designers about more brief about the project = WE ONLY NEED A RESPONSIVE THEME FOR OUR OPEN CART BASE eCommerce WebSite . Mainly item page & product page needs a good unique design. Lighter, speed load, compatible with all browsers and responsive will be appreciated . To Get an idea check on loungerix .co .uk website or tablowmeadows etc.
more projects coming soon .

Our audience will be furniture buying customers .

Furniture

• to get some sort of idea have a look at loungerix .co uk`s website`s listing page and landing page .
• responsive, easy to customize, full theme .

```html
<!DOCTYPE html>
<html lang="en">
<head>
<meta charset="utf-8">
<title>Oakmere Living – Furniture Store Theme</title>
<link rel="stylesheet" href="https://fonts.googleapis.com/css2?family=Barlow:wght@400;500;600&family=Raleway:wght@300;400&display=swap">
<style>
  :root{
    --pink:#e0245e;
    --pink-dark:#c61a50;
    --teal:#19b2c4;
    --teal-dark:#1197a8;
    --ink:#222222;
    --grey:#6b6b6b;
    --line:#e2e2e2;
    --paper:#ffffff;
    --backdrop:#ffffff;
    --sofa:#d71d24;
    --leather:#3a2b27;
    --cream:#fde39a;
    --rust:#b5301b;
  }
  *{box-sizing:border-box;margin:0;padding:0}
  html,body{width:1200px;height:3600px;overflow:hidden;background:var(--backdrop)}
  body{font-family:"Barlow",Arial,sans-serif;color:var(--ink);position:relative}

  /* brand mark */
  .brand-mark{position:absolute;left:100px;top:70px;display:flex;align-items:center;gap:36px}
  .brand-mark .square{width:150px;height:150px;border-radius:26px;background:var(--pink)}
  .brand-mark .name{font-family:"Raleway",Arial,sans-serif;font-weight:300;font-size:96px;color:var(--ink);white-space:nowrap}

  /* page */
  .page{position:absolute;left:100px;top:480px;width:1000px;height:1300px;background:var(--paper);box-shadow:0 10px 40px rgba(0,0,0,.25);overflow:hidden}

  .topbar{height:36px;background:var(--pink);color:#fff;font-size:12px;font-weight:500;display:flex;align-items:center;justify-content:flex-end;padding-right:30px;gap:26px}
  .topbar .account span{margin:0 10px}
  .topbar .phone{display:flex;align-items:center;gap:8px}
  .topbar .search{width:190px;height:20px;border-bottom:1px solid rgba(255,255,255,.7);display:flex;align-items:center;justify-content:space-between;font-weight:400}

  .header{position:relative;height:400px}
  .site-logo{position:absolute;left:22px;top:26px;display:flex;align-items:center;gap:8px}
  .site-logo .square{width:30px;height:30px;border-radius:6px;background:var(--pink)}
  .site-logo .name{font-family:"Raleway",Arial,sans-serif;font-weight:300;font-size:21px;color:var(--ink);white-space:nowrap}

  .main-nav{position:absolute;left:250px;top:30px;width:726px;height:28px;background:var(--teal);display:flex;align-items:center;color:#fff;font-size:12px;font-weight:500}
  .main-nav a{color:#fff;text-decoration:none;width:125px;text-align:center;border-right:1px solid rgba(255,255,255,.35)}
  .main-nav .cart{margin-left:auto;padding-right:40px;display:flex;align-items:center;gap:10px}

  .hero-copy{position:absolute;left:40px;top:105px;width:420px}
  .hero-copy h1{font-family:"Raleway",Arial,sans-serif;font-weight:300;font-size:56px;color:var(--pink);line-height:1.1;white-space:nowrap}
  .hero-copy h1 b{font-weight:300;color:var(--teal)}
  .hero-copy p{margin-top:14px;font-size:15px;line-height:1.75;color:var(--ink)}
  .btn{display:inline-block;border-radius:5px;color:#fff;font-weight:600;text-align:center}
  .btn-pink{background:var(--pink);box-shadow:0 3px 0 var(--pink-dark)}
  .hero-copy .btn{margin:22px 0 0 150px;width:110px;height:28px;line-height:28px;font-size:12px}

  .hero-visual{position:absolute;left:450px;top:75px;width:460px;height:295px;border-radius:50% 50% 18px 18px;background:radial-gradient(ellipse at 50% 40%,#ff4a45 0%,var(--sofa) 55%,#9c1116 100%)}
  .hot-item{position:absolute;left:640px;top:250px;width:270px;padding:8px 14px;background:var(--teal);color:#fff;opacity:.92}
  .hot-item strong{display:block;font-weight:500;font-size:22px}
  .hot-item span{font-size:17px}
  .hot-item-cta{position:absolute;left:790px;top:323px;width:150px;height:36px;line-height:36px;font-size:22px;font-weight:500;border-radius:0;box-shadow:none}

  .divider{height:14px;border-top:5px solid var(--pink);border-bottom:5px solid var(--teal);background:var(--paper)}

  .content{position:relative;height:660px;display:flex}
  .sidebar{width:230px;padding:40px 0 0 24px;border-right:1px solid var(--line)}
  .sidebar h3{width:185px;height:28px;line-height:28px;background:var(--teal);color:#fff;font-size:13px;font-weight:600;text-align:center}
  .sidebar ul{list-style:none;margin-top:10px;width:185px}
  .sidebar li{font-size:14px;color:var(--grey);padding-left:45px;line-height:24px}
  .sidebar li.group{padding-left:0;color:var(--teal);font-weight:600;border-top:1px solid var(--line);margin-top:4px}
  .sidebar li.group:first-child{border-top:0;margin-top:0}

  .product{position:relative;flex:1}
  .product h2{position:absolute;left:30px;top:48px;font-size:26px;font-weight:500;letter-spacing:.5px}
  .product .desc{position:absolute;left:30px;top:95px;width:200px;font-size:13px;line-height:1.65;color:var(--grey)}
  .add-cart{position:absolute;left:30px;top:285px;width:190px;height:36px;background:var(--teal);color:#fff;display:flex;align-items:center;font-size:15px;font-weight:600}
  .add-cart .icon{width:44px;height:36px;display:flex;align-items:center;justify-content:center;border-right:1px solid rgba(255,255,255,.35)}
  .add-cart span{flex:1;text-align:center}
  .colors{position:absolute;left:30px;top:342px}
  .colors h4{font-size:19px;font-weight:500}
  .swatches{display:flex;gap:14px;margin-top:10px}
  .swatches i{width:44px;height:44px;border-radius:11px;display:block}

  .product-visual{position:absolute;left:290px;top:130px;width:370px;height:270px;border-radius:40% 60% 20% 30%;background:radial-gradient(ellipse at 40% 40%,#5b4741 0%,var(--leather) 60%,#1e1512 100%)}
  .price-badge{position:absolute;left:585px;top:55px;width:118px;height:118px;border-radius:50%;background:var(--teal);border:5px solid #fff;box-shadow:0 3px 8px rgba(0,0,0,.25);color:#fff;font-size:30px;font-weight:500;display:flex;align-items:center;justify-content:center}
  .delivery-badge{position:absolute;left:678px;top:145px;width:62px;height:62px;border-radius:50%;background:var(--pink);border:3px solid #fff;box-shadow:0 2px 6px rgba(0,0,0,.25);color:#fff;font-size:11px;line-height:1.2;text-align:center;display:flex;align-items:center;justify-content:center}

  .carousel-arrows{position:absolute;right:30px;top:432px;display:flex;gap:4px}
  .carousel-arrows span{width:20px;height:20px;background:var(--teal);display:flex;align-items:center;justify-content:center}
  .related{position:absolute;left:10px;top:462px;display:flex;gap:18px;border-top:1px solid var(--line);padding-top:16px;width:750px}
  .card{position:relative;width:170px;height:150px;border:1px solid var(--line);border-radius:5px;box-shadow:0 2px 5px rgba(0,0,0,.1)}
  .card .thumb{position:absolute;left:35px;top:15px;width:100px;height:115px;border-radius:12px}
  .card .tag{position:absolute;left:0;bottom:14px;background:var(--teal);color:#fff;font-size:12px;font-weight:600;padding:3px 12px}

  .footer{position:absolute;left:0;bottom:0;width:1000px;height:180px;background:var(--pink);border-top:5px solid var(--teal)}
  .footer nav{position:absolute;left:240px;bottom:36px;display:flex;gap:100px;font-size:12px;font-weight:500}
  .footer nav a{color:#fff;text-decoration:none}
</style>
</head>
<body>

<div class="brand-mark">
  <div class="square"></div>
  <div class="name">Oakmere Living</div>
</div>

<main class="page">
  <div class="topbar">
    <div class="account">SIGN IN<span>|</span>SIGN UP</div>
    <div class="phone">
      <svg width="14" height="14" viewBox="0 0 24 24"><path fill="#fff" d="M6.6 10.8a15.1 15.1 0 0 0 6.6 6.6l2.2-2.2c.3-.3.7-.4 1-.2 1.1.4 2.3.6 3.6.6.6 0 1 .4 1 1V20c0 .6-.4 1-1 1A17 17 0 0 1 3 4c0-.6.4-1 1-1h3.5c.6 0 1 .4 1 1 0 1.3.2 2.5.6 3.6.1.3 0 .7-.2 1z"/></svg>
      +100 2468 13579
    </div>
    <div class="search">Search
      <svg width="11" height="11" viewBox="0 0 24 24"><circle cx="10" cy="10" r="7" fill="none" stroke="#fff" stroke-width="3"/><path d="M15 15l7 7" stroke="#fff" stroke-width="3"/></svg>
    </div>
  </div>

  <header class="header">
    <div class="site-logo">
      <div class="square"></div>
      <div class="name">Oakmere Living</div>
    </div>
    <nav class="main-nav">
      <a>HOME</a><a>PRODUCTS</a><a>CATEGORIES</a><a>CONTACT US</a>
      <div class="cart">
        <svg width="16" height="14" viewBox="0 0 24 20"><path fill="#fff" d="M0 1h4l3 11h13l3-8H7.5L6.8 1.5 6 0H0zM9 15a2 2 0 1 0 0 4 2 2 0 0 0 0-4zm10 0a2 2 0 1 0 0 4 2 2 0 0 0 0-4z"/></svg>
        2 ITEMS
      </div>
    </nav>

    <div class="hero-copy">
      <h1>Oakmere <b>Living</b></h1>
      <p>Lorem ipsum dolor sit amet,<br>consectetuer adipiscing elit. Aenean<br>commodo ligula eget dolor. Aenean<br>massa. Cum sociis natoque penatibus</p>
      <span class="btn btn-pink">Shop Now</span>
    </div>

    <div class="hero-visual" role="img" aria-label="Red curved designer sofa on wooden legs"></div>
    <div class="hot-item"><strong>HOT ITEM</strong><span>50% discount, Free delivery</span></div>
    <span class="btn btn-pink hot-item-cta">Get It Now</span>
  </header>

  <div class="divider"></div>

  <section class="content">
    <aside class="sidebar">
      <h3>Select Category</h3>
      <ul>
        <li class="group">Chairs</li><li>Chairs</li><li>Chairs</li><li>Chairs</li><li>Chairs</li>
        <li class="group">Tables</li><li>Tables</li><li>Tables</li><li>Tables</li>
        <li class="group">Tables</li><li>Tables</li><li>Tables</li><li>Tables</li>
        <li class="group">Tables</li><li>Tables</li><li>Tables</li><li>Tables</li>
      </ul>
    </aside>

    <div class="product">
      <h2>THE KING'S</h2>
      <p class="desc">Lorem ipsum dolor sit amet, consectetuer adipiscing elit. Aenean commodo ligula eget dolor. Aenean massa. Cum sociis natoque penatibus et magnis dis parturient montes, nascetur ridiculus mus. Lorem ipsum</p>
      <div class="add-cart">
        <div class="icon"><svg width="18" height="15" viewBox="0 0 24 20"><path fill="#fff" d="M0 1h4l3 11h13l3-8H7.5L6.8 1.5 6 0H0zM9 15a2 2 0 1 0 0 4 2 2 0 0 0 0-4zm10 0a2 2 0 1 0 0 4 2 2 0 0 0 0-4z"/></svg></div>
        <span>Add to Cart</span>
      </div>
      <div class="colors">
        <h4>AVAILABLE COLORS</h4>
        <div class="swatches"><i style="background:var(--leather)"></i><i style="background:var(--cream)"></i><i style="background:var(--rust)"></i></div>
      </div>

      <div class="product-visual" role="img" aria-label="Dark brown leather lounge chair on a chrome base"></div>
      <div class="price-badge">$28.99</div>
      <div class="delivery-badge">Free<br>Delivery</div>

      <div class="carousel-arrows">
        <span><svg width="8" height="10" viewBox="0 0 8 10"><path d="M6 1L2 5l4 4" fill="none" stroke="#fff" stroke-width="2"/></svg></span>
        <span><svg width="8" height="10" viewBox="0 0 8 10"><path d="M2 1l4 4-4 4" fill="none" stroke="#fff" stroke-width="2"/></svg></span>
      </div>
      <div class="related">
        <div class="card"><div class="thumb" role="img" aria-label="Dark lounge armchair" style="background:linear-gradient(160deg,#4a3a35,#1f1715)"></div><span class="tag">39.99$</span></div>
        <div class="card"><div class="thumb" role="img" aria-label="Grey club armchair" style="background:linear-gradient(160deg,#6d6f72,#3b3d40)"></div><span class="tag">39.99$</span></div>
        <div class="card"><div class="thumb" role="img" aria-label="White egg chair" style="background:linear-gradient(160deg,#ffffff,#cfd2d4)"></div><span class="tag">39.99$</span></div>
        <div class="card"><div class="thumb" role="img" aria-label="Red egg chair" style="background:linear-gradient(160deg,#ef4a33,#a9190f)"></div><span class="tag">39.99$</span></div>
      </div>
    </div>
  </section>

  <footer class="footer">
    <nav><a>HOME</a><a>PRODUCTS</a><a>CATEGORIES</a><a>CONTACT US</a></nav>
  </footer>
</main>

</body>
</html>
```